New Business Card Design Project VORASTI-Italy

we are VORASTI-Italy
our company in the market for 3 years we are luxury cosmetic company and its about time for a facelift :)
i will like to have elegant luxurious and unique business card
that will give the person that get it a unique, luxurious and elegant impression
I'm VERY OPEN FOR NEW IDEAS , even duo i add a few files of things that i see on line and i like them

i add my logo as well
my website is VORASTI.COM
(if you would like to see the main style that we have)

Target Market(s)

adult that have money :)

Industry/Entity Type

Business

Contact Information for Business Card

Name - Paul Vorasti
Position - CEO and CO Founder
address - 4817 E Larkdale
telephone - 555-384-1962
email - paul@vorasti.com
fax - 555-384-1962
website - VORASTI.COM

Colors
000000
959595
fbee3e
ffffff

Requirements
Must have
• big logo in GOLD color
• elegant look
• impressive
Nice to have
• not must but maybe classy pattern background
• not must but maybe emblem
• maybe clear plastic business card
Should not have
• colors
• images

```html
<!DOCTYPE html>
<html lang="en">
<head>
<meta charset="utf-8">
<title>VORASTI Business Card</title>
<link rel="stylesheet" href="https://fonts.googleapis.com/css2?family=Exo+2:wght@400;600;700&display=swap">
<style>
  :root {
    --stage: #d3d3d7;
    --card: #2b2b2c;
    --card-deep: #262627;
    --stitch-tone: #4a4a4c;
    --gold: #c9a83e;
    --name-grey: #b9b9bb;
    --text-grey: #a4a4a6;
  }
  * { margin: 0; padding: 0; box-sizing: border-box; }
  html, body {
    width: 1200px;
    height: 1200px;
    overflow: hidden;
    background: var(--stage);
    font-family: "Exo 2", sans-serif;
  }
  .canvas { position: relative; width: 1200px; height: 1200px; }
  .card {
    position: absolute;
    left: 229px;
    width: 741px;
    height: 413px;
    border-radius: 16px;
    background: var(--card);
    overflow: hidden;
  }
  .card-front { top: 146px; }
  .card-back { top: 626px; }
  .front-pattern {
    position: absolute;
    inset: 0;
    background:
      radial-gradient(ellipse at 50% 50%, var(--stitch-tone) 0%, var(--card) 55%, var(--card-deep) 100%);
  }
  .front-mark {
    position: absolute;
    left: 222px;
    top: 58px;
    width: 296px;
    height: 296px;
    border: 6px solid var(--gold);
    border-radius: 50%;
    background: var(--card);
    display: flex;
    align-items: center;
    justify-content: center;
  }
  .front-name {
    font-weight: 600;
    font-size: 48px;
    letter-spacing: 2px;
    color: var(--gold);
  }
  .holder-name {
    position: absolute;
    left: 55px;
    top: 46px;
    font-weight: 700;
    font-size: 40px;
    color: var(--name-grey);
  }
  .holder-title {
    position: absolute;
    left: 58px;
    top: 101px;
    font-weight: 400;
    font-size: 24px;
    color: var(--text-grey);
  }
  .contact-list {
    position: absolute;
    left: 55px;
    top: 226px;
    list-style: none;
    font-size: 20px;
    line-height: 1;
    color: var(--text-grey);
  }
  .contact-list li { height: 28px; }
  .contact-list li:nth-child(2) { height: 25px; }
  .contact-list li:nth-child(3) { height: 30px; }
  .back-mark {
    position: absolute;
    left: 535px;
    top: 250px;
    width: 160px;
    display: flex;
    flex-direction: column;
    align-items: center;
  }
  .back-mark-circle {
    width: 60px;
    height: 60px;
    border: 3px solid var(--gold);
    border-radius: 50%;
    margin-bottom: 8px;
  }
  .back-mark-name {
    font-weight: 600;
    font-size: 28px;
    letter-spacing: 1px;
    color: var(--gold);
  }
</style>
</head>
<body>
<main class="canvas">
  <section class="card card-front">
    <div class="front-pattern" role="img" aria-label="Quilted diamond stitch pattern in soft grey on charcoal"></div>
    <div class="front-mark">
      <span class="front-name">VORASTI</span>
    </div>
  </section>

  <section class="card card-back">
    <h1 class="holder-name">PAUL VORASTI</h1>
    <p class="holder-title">CEO and CO Founder</p>
    <ul class="contact-list">
      <li>4817 E Larkdale</li>
      <li>555-384-1962</li>
      <li>&nbsp;paul@vorasti.com</li>
      <li>555-384-1962</li>
      <li>Vorasti . com</li>
    </ul>
    <div class="back-mark">
      <span class="back-mark-circle"></span>
      <span class="back-mark-name">VORASTI</span>
    </div>
  </section>
</main>
</body>
</html>
```